VANTA SWEEP

Need a professional looking business card that can fit : Name, Title, Cell, and office phone numbers. On the flip side we would like a list of our services : Highway accident management and towing, Crime scene clean up, Illegal drug lab clean up, Drug disposal, and Hazardous materials clean up.

```html
<!DOCTYPE html>
<html lang="en">
<head>
<meta charset="utf-8">
<title>Vanta Sweep — Business Card</title>
<link rel="stylesheet" href="https://fonts.googleapis.com/css2?family=Cinzel:wght@600;700&family=Open+Sans:wght@400;600&display=swap">
<style>
  :root {
    --page: #e9e6e1;
    --card-black: #0b0d10;
    --card-black-2: #1a1d22;
    --band-blue: #1d4a78;
    --band-blue-dark: #10304f;
    --gold: #e7c43a;
    --gold-soft: #d9b531;
    --rule-blue: #2f6aa6;
    --white: #f4f4f4;
  }
  * { margin: 0; padding: 0; box-sizing: border-box; }
  html, body { width: 1200px; height: 1023px; overflow: hidden; background: var(--page); }
  .canvas { width: 1200px; height: 1023px; display: flex; align-items: center; justify-content: center; }
  .card {
    position: relative; width: 900px; height: 514px; overflow: hidden;
    background: linear-gradient(160deg, var(--card-black-2), var(--card-black) 60%);
    border-radius: 4px; box-shadow: 0 10px 30px rgba(0,0,0,.25);
  }
  .brand-mark {
    position: absolute; left: 40px; top: 150px; width: 260px;
    display: flex; align-items: center; gap: 12px;
  }
  .brand-dot { width: 28px; height: 28px; border-radius: 50%; background: var(--gold); flex: none; }
  .brand-name { font-family: 'Cinzel', serif; font-weight: 700; font-size: 26px; color: var(--gold); letter-spacing: 1px; }
  .header { position: absolute; left: 330px; right: 40px; top: 34px; text-align: center; }
  .company { font-family: 'Cinzel', serif; font-weight: 700; font-size: 50px; color: var(--gold); letter-spacing: 2px; line-height: 1; }
  .region { font-family: 'Cinzel', serif; font-weight: 600; font-size: 20px; color: var(--gold); letter-spacing: 3px; margin-top: 8px; }
  .rule { height: 2px; background: var(--rule-blue); margin: 18px auto; width: 86%; }
  .person { font-family: 'Cinzel', serif; font-weight: 700; font-size: 30px; color: var(--gold); letter-spacing: 1.5px; }
  .title { font-family: 'Open Sans', sans-serif; font-weight: 600; font-size: 14px; color: var(--white); letter-spacing: 1px; margin-top: 6px; }
  .band {
    position: absolute; left: 0; right: 0; bottom: 0; height: 214px;
    background: linear-gradient(100deg, var(--band-blue) 0%, var(--band-blue-dark) 100%);
    border-top: 4px solid var(--gold);
    display: flex; padding: 36px 48px 0;
  }
  .band::before { content: ""; position: absolute; left: 0; right: 0; top: 6px; height: 2px; background: var(--gold-soft); }
  .contacts { list-style: none; width: 400px; }
  .contacts li { display: flex; align-items: center; gap: 12px; font-family: 'Open Sans', sans-serif; font-size: 20px; color: var(--white); margin-bottom: 10px; }
  .contacts svg { width: 22px; height: 22px; flex: none; }
  .services { list-style: none; }
  .services li { font-family: 'Open Sans', sans-serif; font-size: 19px; color: var(--gold); margin-bottom: 9px; display: flex; align-items: center; gap: 10px; }
  .services li::before { content: ""; width: 9px; height: 9px; border-radius: 50%; background: var(--gold); flex: none; }
</style>
</head>
<body>
<main class="canvas">
  <article class="card">
    <div class="brand-mark">
      <span class="brand-dot"></span>
      <span class="brand-name">VANTA SWEEP</span>
    </div>

    <header class="header">
      <h1 class="company">VANTA SWEEP</h1>
      <p class="region">★ WEST VIRGINIA ★</p>
      <div class="rule"></div>
      <h2 class="person">DANIEL MARLOWE</h2>
      <p class="title">DIRECTOR</p>
      <div class="rule"></div>
    </header>

    <section class="band">
      <ul class="contacts">
        <li>
          <svg viewBox="0 0 22 22"><circle cx="11" cy="11" r="11" fill="#e7c43a"/><path d="M7 6.5c.6-.6 1.4-.5 1.8.1l1 1.5c.3.5.2 1-.2 1.4l-.6.5c.6 1.3 1.6 2.3 2.9 2.9l.5-.6c.4-.4.9-.5 1.4-.2l1.5 1c.6.4.7 1.2.1 1.8-1 1-2.6 1.1-4.3.1-1.6-.9-3-2.3-3.9-3.9-1-1.7-.9-3.3.1-4.3z" fill="#10304f"/></svg>
          (555) 410-2281
        </li>
        <li>
          <svg viewBox="0 0 22 22"><circle cx="11" cy="11" r="11" fill="#e7c43a"/><rect x="7.5" y="5" width="7" height="12" rx="1.2" fill="#10304f"/><rect x="8.7" y="6.5" width="4.6" height="7.5" fill="#e7c43a"/></svg>
          (555) 410-2297
        </li>
        <li>
          <svg viewBox="0 0 22 22"><circle cx="11" cy="11" r="11" fill="#e7c43a"/><rect x="6" y="9" width="10" height="7" rx="1" fill="#10304f"/><rect x="8" y="5.5" width="6" height="4" fill="#10304f"/></svg>
          (555) 736-9043
        </li>
        <li>
          <svg viewBox="0 0 22 22"><circle cx="11" cy="11" r="11" fill="#e7c43a"/><rect x="5.5" y="7" width="11" height="8" rx="1" fill="#10304f"/><path d="M6 7.5l5 4 5-4" stroke="#e7c43a" stroke-width="1.2" fill="none"/></svg>
          daniel.marlowe@vantasweep.com
        </li>
      </ul>
      <ul class="services">
        <li>Highway Accident Management &amp; Towing</li>
        <li>Crime Scene Clean Up</li>
        <li>Illegal Drug Lab Clean Up</li>
        <li>Drug Disposal</li>
        <li>Hazardous Materials Clean Up</li>
      </ul>
    </section>
  </article>
</main>
</body>
</html>
```